CORALSpath Books Needs a Book Cover Design

We need a book cover design for an inspirational, motivational nugget book. It's another part of a series of small 1-paragraph chapter books with lots of quotes. It is a spiritual book and we would like to see designs that depict peace through a storm. The final design should communicate peace or calm through violent storms of life--adversity, setbacks, and sorrow.
The book size is 5.5 x 8.5 ins and the number of pages is 96.
Reason: To be able to allow for more submissions.
Target Market(s)
General reading audience
Look and feel
Each slider illustrates characteristics of the customer's brand and the style your logo design should communicate.

```html
<!DOCTYPE html>
<html lang="en">
<head>
<meta charset="utf-8">
<title>Peace through the Storms — Book Cover</title>
<link rel="stylesheet" href="https://fonts.googleapis.com/css2?family=Merriweather:ital,wght@1,400;1,700&family=Arimo:wght@700&display=swap">
<style>
  :root {
    --page-bg: #f2f2f0;
    --wave-deep: #123f3c;
    --wave-teal: #2f7a72;
    --wave-sea: #3f9a92;
    --wave-mist: #9fb8a6;
    --light-haze: #f1f3de;
    --foam: #e8efe6;
    --earth-light: #d8b489;
    --earth-mid: #b98c5e;
    --earth-dark: #7d5634;
    --title-white: #ffffff;
    --author-yellow: #f4e21c;
  }
  * { margin: 0; padding: 0; box-sizing: border-box; }
  html, body {
    width: 983px;
    height: 1200px;
    overflow: hidden;
    background: var(--page-bg);
  }
  .canvas {
    position: relative;
    width: 983px;
    height: 1200px;
    display: flex;
    align-items: center;
    justify-content: center;
  }
  .book-cover {
    position: relative;
    width: 712px;
    height: 1100px;
    overflow: hidden;
    background: var(--wave-deep);
  }
  .cover-art {
    position: absolute;
    inset: 0;
    background:
      /* glow at the far end of the path */
      radial-gradient(ellipse 26% 30% at 62% 40%, rgba(248,250,232,0.95) 0%, rgba(241,243,222,0.55) 50%, rgba(241,243,222,0) 100%),
      /* dry path narrowing into the distance */
      radial-gradient(ellipse 42% 48% at 52% 100%, var(--earth-mid) 0%, rgba(216,180,137,0.9) 55%, rgba(216,180,137,0) 100%),
      /* foam line where the water meets the path */
      radial-gradient(ellipse 58% 42% at 50% 100%, rgba(232,239,230,0) 62%, rgba(232,239,230,0.75) 70%, rgba(232,239,230,0) 80%),
      /* left wall of water */
      linear-gradient(100deg, var(--wave-deep) 0%, var(--wave-teal) 18%, var(--wave-sea) 30%, rgba(63,154,146,0) 48%),
      /* right wall of water, paler and misty */
      linear-gradient(260deg, #5f8f7e 0%, var(--wave-mist) 14%, rgba(159,184,166,0) 34%),
      /* overall sky-to-earth tones */
      linear-gradient(180deg, #2b6a60 0%, #7fa897 22%, var(--light-haze) 45%, var(--earth-light) 70%, var(--earth-dark) 100%);
  }
  .title-block {
    position: absolute;
    top: 250px;
    right: 96px;
    text-align: right;
    color: var(--title-white);
    font-family: "Merriweather", Georgia, serif;
    font-style: italic;
    text-shadow: 0 2px 10px rgba(30,60,55,0.35);
    line-height: 1;
  }
  .title-main {
    display: block;
    font-weight: 700;
  }
  .title-peace {
    font-size: 116px;
    margin-right: 40px;
  }
  .title-link {
    display: block;
    font-weight: 400;
    font-size: 44px;
    margin: 4px 0 0 0;
  }
  .title-storms {
    font-size: 128px;
    margin-top: -8px;
    letter-spacing: -1px;
  }
  .author-name {
    position: absolute;
    left: 74px;
    bottom: 54px;
    font-family: "Arimo", Arial, sans-serif;
    font-weight: 700;
    font-size: 25px;
    letter-spacing: 0.3px;
    color: var(--author-yellow);
  }
</style>
</head>
<body>
  <main class="canvas">
    <article class="book-cover">
      <div class="cover-art" role="img" aria-label="Towering storm waves parted into two walls of teal sea water, with a lone traveller carrying a backpack walking along a path of cracked dry earth between them toward soft light"></div>
      <h1 class="title-block">
        <span class="title-main title-peace">Peace</span>
        <span class="title-link">through the</span>
        <span class="title-main title-storms">Storms</span>
      </h1>
      <p class="author-name">FIRST NAME SECOND NAME OF AUTHOR</p>
    </article>
  </main>
</body>
</html>
```